Brandt WordPress Design Contest

We need a wordpress design that will incorporate a professional color scheme with company logo in a clean layout. The design needs to consider that this will be developed on a responsive theme. Colors are up to the designer - The green of the logo with black, gray or an accent color. Client wants a 'modern' look.

Industry/Entity Type

It Company

Number of Pages Required

1 page

Font styles to use
Serif
Sans Serif

Requirements
Must have
• Navigation: 1) Home 2) All Auctions 3) Real Estate for Sale 4) Services 5) About Us 6) Contact Us
• Colors - a corporate look with professional color scheme. Green of logo + black and gray, or an eggshell/light beige, or any other accent that keeps within a corporate look.
• In header - logo (attached) , and contact info :5127 Old Harrow Lane, Alder Falls, NV 89410
• 270-555-3946
• Fax: 270-555-3947
• Email:info@brandtpropertybidhouse.example
• Design will feature a full width (960 px) slideshow - use a stock photo for real estate.
• Widgets in sidebar or where appropriate - 1) Email Signup 2) Message of the Day 3) Upcoming Auctions 4) News&Events blog 5) Testimonials 6) Social media - FB, twitter, youtube, pinterest, google+
• Footer will have company logo, association logos (attached) and contact info, with another widget area if necessary
Nice to have
• use of drop down menu styling - Upcoming Auctions / Online Auctions/ Past Auctions under the "Auction Calendar" menu item

```html
<!DOCTYPE html>
<html lang="en">
<head>
<meta charset="utf-8">
<title>Brandt Real Estate &amp; Auction</title>
<link href="https://fonts.googleapis.com/css2?family=Lato:ital,wght@0,400;0,700;0,900;1,400;1,700&family=Oswald:wght@400;500&display=swap" rel="stylesheet">
<style>
:root{
  --green:#0b6b36;
  --green-dark:#075229;
  --green-text:#0f6f38;
  --ink:#222;
  --muted:#666;
  --line:#dcdcdc;
  --card-line:#e2e2e2;
  --footer-dark:#2b2b2b;
  --footer-bottom:#232323;
  --white:#fff;
}
*{box-sizing:border-box;margin:0;padding:0}
html,body{width:732px;height:1200px;overflow:hidden;background:var(--white)}
body{position:relative;font-family:'Lato',sans-serif;color:var(--ink)}
.abs{position:absolute}
.top-rule{left:0;top:0;width:732px;height:3px;background:var(--green)}

/* header */
.brand{left:80px;top:14px;display:flex;align-items:center;gap:7px}
.brand-square{width:22px;height:22px;background:var(--green)}
.brand-name{font-family:'Lato',sans-serif;font-weight:900;font-size:30px;color:var(--green);letter-spacing:.5px}
.contact-top{right:80px;top:8px;text-align:right;font-size:10.5px;color:var(--ink)}
.contact-top div{display:flex;align-items:center;justify-content:flex-end;gap:6px;height:19px}
.contact-top svg{fill:var(--green)}
.nav{left:254px;top:54px;display:flex;font-size:8.5px;font-weight:400}
.nav a{color:var(--ink);text-decoration:none;height:20px;line-height:20px;padding:0 11px;margin-right:4px}
.nav a.active{background:var(--green);color:var(--white);border-radius:7px 7px 0 0;padding:0 11px;font-weight:700}

/* slider */
.slider{left:80px;top:82px;width:572px;height:239px;background:linear-gradient(160deg,#d9dccd 0%,#b7ad93 30%,#8a6b55 55%,#c9484b 78%,#6e7a52 100%)}
.slide-caption{left:422px;top:129px;width:175px;height:79px;background:rgba(235,235,230,.88);padding:9px 12px;font-family:'Oswald',sans-serif;font-size:15.5px;line-height:21px;color:var(--green);}
.slide-arrow{top:189px;width:17px;height:25px;background:#e9e9e9;display:flex;align-items:center;justify-content:center}
.slide-arrow svg{stroke:#222;stroke-width:2;fill:none}

/* welcome */
.welcome{left:96px;top:336px;width:540px;text-align:center}
.welcome h1{font-size:14.5px;font-weight:700;color:var(--green);letter-spacing:.2px}
.welcome p{margin-top:7px;font-size:8.8px;line-height:13.6px;color:#333}
.btn-outline{left:332px;top:410px;width:68px;height:22px;border:1px solid var(--green);border-radius:3px;color:var(--green);font-size:10px;font-weight:700;display:flex;align-items:center;justify-content:center}

/* section bars */
.bar{left:80px;width:351px;height:23px;background:var(--green);color:var(--white);font-size:11.5px;font-weight:700;padding-left:7px;line-height:23px}
.bar-arrows{position:absolute;right:9px;top:0;display:flex;gap:9px;height:23px;align-items:center}
.bar-arrows svg{stroke:#fff;stroke-width:2.2;fill:none}

.card{width:109px;height:133px;border:1px solid var(--card-line);padding:5px}
.thumb{width:97px;height:68px;border:1px solid #ccc}
.price{margin-top:4px;font-size:10.5px;font-weight:700;color:var(--green-text)}
.desc{margin-top:2px;font-size:7.3px;font-weight:700;color:#222}
.info{margin-top:6px;width:35px;height:18px;background:var(--green);color:var(--white);font-size:7.5px;font-weight:700;display:flex;align-items:center;justify-content:center}

/* testimonials */
.testi-head{left:80px;top:826px;width:351px;height:26px;border-bottom:1px solid var(--line);display:flex;align-items:center;gap:7px}
.testi-head h2{font-size:11.5px;font-weight:700;color:var(--green)}
.testi-head::after{content:"";position:absolute;left:0;bottom:-2px;width:77px;height:2px;background:var(--green)}
.testi-arrows{left:414px;top:834px;display:flex;gap:5px}
.testi-arrows svg{fill:none;stroke-width:1.4}
.avatar{left:80px;top:864px;width:58px;height:58px;border-radius:50%;border:3px solid var(--green);background:radial-gradient(circle at 50% 45%,#e8c9ad 0%,#c99e80 45%,#dcdcdc 75%)}
.testi-name{left:152px;top:879px;font-size:9.5px;font-weight:700;color:var(--green)}
.testi-role{left:152px;top:893px;font-size:7.3px;font-style:italic;color:#444}
.testi-quote{left:80px;top:930px;width:355px;font-size:8.2px;line-height:16px;font-style:italic;color:#444}
.testi-quote .mark{font-size:17px;color:#aaa;font-style:normal;line-height:8px;vertical-align:-4px;margin-right:3px}

/* sidebar */
.video-box{left:453px;top:457px;width:199px;height:149px;border:1px solid var(--card-line);padding:2px}
.side-head{height:24px;background:var(--green);color:var(--white);font-size:10px;font-weight:700;padding-left:7px;line-height:24px;position:relative}
.video-frame{margin-top:3px;height:103px;background:linear-gradient(170deg,#6f7276 0%,#3a3d40 55%,#1f2123 100%);display:flex;align-items:center;justify-content:center}
.play{width:22px;height:22px;border-radius:50%;background:rgba(255,255,255,.25);display:flex;align-items:center;justify-content:center}
.video-controls{height:16px;background:#1a1a1a;display:flex;align-items:center;gap:6px;padding:0 6px;font-size:6.5px;color:#fff}
.track{flex:1;height:3px;background:#555;border-radius:2px;position:relative}
.track::before{content:"";position:absolute;left:0;top:0;width:78%;height:3px;background:#333}

.motd{left:453px;top:626px;width:199px;height:49px;background:var(--green);color:var(--white);padding:3px 6px}
.motd h3{font-size:16.5px;font-style:italic;font-weight:700;letter-spacing:-.2px}
.motd p{font-size:7.3px;line-height:11.5px;margin-top:2px;width:165px}
.motd-fold{right:0;top:0;width:0;height:0;border-top:14px solid var(--white);border-left:14px solid transparent}
.motd svg{position:absolute;right:7px;bottom:7px;stroke:#fff;stroke-width:2;fill:none}

.news{left:453px;top:693px;width:199px;height:280px;border:1px solid var(--card-line);padding:2px}
.view-all{position:absolute;right:6px;top:0;font-size:7px;font-style:italic}
.news-item{position:absolute;left:3px;width:190px;height:50px}
.news-item.sep{border-bottom:1px dashed #cfcfcf}
.date{position:absolute;left:0;top:4px;width:30px;height:33px}
.date .day{height:21px;background:#e4e4e4;font-size:12px;font-weight:700;color:#333;text-align:center;line-height:21px}
.date .mon{height:12px;background:var(--green);color:#fff;font-size:7px;text-align:center;line-height:12px}
.news-title{position:absolute;left:42px;top:5px;font-size:8.3px;font-weight:700;color:var(--green)}
.news-text{position:absolute;left:42px;top:18px;font-size:7.3px;color:#888}
.news-more{position:absolute;left:42px;top:30px;font-size:7px;font-style:italic;color:var(--green);text-decoration:underline}

/* footer */
.foot-band{left:0;top:998px;width:732px;height:36px;background:var(--green)}
.foot-band h4{position:absolute;top:11px;font-size:10.5px;font-weight:700;color:var(--white)}
.foot-dark{left:0;top:1034px;width:732px;height:131px;background:var(--footer-dark)}
.foot-bottom{left:0;top:1165px;width:732px;height:35px;background:var(--footer-bottom);border-top:1px solid #3a3a3a}
.quick{left:81px;top:1043px;width:100px;border-right:1px solid #3a3a3a;height:110px}
.quick li{list-style:none;font-size:7.8px;color:#e6e6e6;height:18.4px;line-height:18.4px}
.quick li::before{content:"›";color:#888;margin-right:8px}
.aff{left:202px;top:1043px;width:95px;height:101px;background:var(--white);display:flex;flex-direction:column;align-items:center;justify-content:center;gap:7px}
.aff span{display:block;width:54px;height:22px;background:#cfcfcf}
.fcontact{left:340px;top:1043px;font-size:7.8px;color:#e6e6e6;line-height:12px}
.fcontact .row{display:flex;align-items:center;gap:6px;position:absolute;left:0;white-space:nowrap}
.fcontact svg{fill:#999}
.newsletter{left:518px;top:1043px;width:134px;font-size:7.8px;color:#e6e6e6;line-height:11.5px}
.field{position:absolute;left:518px;width:133px;height:17px;background:var(--white);border:1px solid #ccc;font-size:7px;font-style:italic;color:#888;padding-left:5px;line-height:15px}
.submit{left:518px;top:1123px;width:60px;height:18px;background:var(--green);border:1px solid #9bc7ac;color:#fff;font-size:8.5px;font-weight:700;display:flex;align-items:center;justify-content:center}
.copy{left:80px;top:1177px;font-size:7.8px;color:#ddd}
.social{top:1172px;width:19px;height:19px;border-radius:50%;background:var(--green);border:1px solid #4a8a62}
</style>
</head>
<body>

<div class="abs top-rule"></div>

<header>
  <div class="abs brand"><span class="brand-square"></span><span class="brand-name">Brandt</span></div>
  <div class="abs contact-top">
    <div><svg width="12" height="12" viewBox="0 0 24 24"><path d="M6.6 10.8a15 15 0 0 0 6.6 6.6l2.2-2.2c.3-.3.7-.4 1-.2 1.1.4 2.3.6 3.6.6.6 0 1 .4 1 1V20c0 .6-.4 1-1 1A17 17 0 0 1 3 4c0-.6.4-1 1-1h3.5c.6 0 1 .4 1 1 0 1.3.2 2.5.6 3.6.1.3 0 .7-.2 1z"/></svg>270-555-3946</div>
    <div><svg width="16" height="11" viewBox="0 0 16 11"><rect x="0" y="0" width="16" height="11" rx="1"/><path d="M1 1l7 5 7-5" stroke="#fff" stroke-width="1.2" fill="none"/></svg>info@brandtpropertybidhouse.example</div>
  </div>
  <nav class="abs nav">
    <a class="active">Home</a><a>All Auctions</a><a>Real Estate for Sale</a><a>Services</a><a>About Us</a><a>Contact Us</a>
  </nav>
</header>

<section>
  <div class="abs slider" role="img" aria-label="Stock photo of a smiling family in front of a house with a sold sign"></div>
  <div class="abs slide-caption">Lorem ipsum dolor sit alm amet consectetuer dolor adipiscing elit sed</div>
  <div class="abs slide-arrow" style="left:78px"><svg width="8" height="12"><path d="M6 1L2 6l4 5"/></svg></div>
  <div class="abs slide-arrow" style="left:638px"><svg width="8" height="12"><path d="M2 1l4 5-4 5"/></svg></div>
</section>

<section class="abs welcome">
  <h1>WELCOME TO BRANDT REAL ESTATE &amp; AUCTION</h1>
  <p>Lorem ipsum dolor sit amet, consectetuer adipiscing elit, sed diam nonummy nibh euismod tincidunt ut laoreet dolore magna aliquam erat volutpat. Ut wisi enim ad minim veniam, quis nostrud exerci tation ullamcorper suscipit lobortis nisl ut aliquip ex ea commodo consequat. Duis autem vel eum iriure dolor in hendrerit in vulputate velit esse</p>
</section>
<div class="abs btn-outline">Read More</div>

<div class="abs bar" style="top:457px">ALL AUCTIONS
  <div class="bar-arrows"><svg width="7" height="10"><path d="M5 1L2 5l3 4"/></svg><svg width="7" height="10"><path d="M2 1l3 4-3 4"/></svg></div>
</div>
<div class="abs card" style="left:80px;top:488px"><div class="thumb" role="img" aria-label="Modern white villa with pool" style="background:linear-gradient(180deg,#8fb5d6,#e6e6e0 55%,#5c8a6a)"></div><div class="price">Prise : $ 12000</div><div class="desc">Lorem ipsum dolor sit</div><div class="info">Info ››</div></div>
<div class="abs card" style="left:201px;top:488px"><div class="thumb" role="img" aria-label="Two-storey house with orange walls" style="background:linear-gradient(180deg,#6aa0d4,#c98a5d 55%,#6d8f4e)"></div><div class="price">Prise : $ 12500</div><div class="desc">Lorem ipsum dolor sit</div><div class="info">Info ››</div></div>
<div class="abs card" style="left:322px;top:488px"><div class="thumb" role="img" aria-label="Cream mansion with swimming pool" style="background:linear-gradient(180deg,#4d8ac9,#e3dcc6 50%,#3aa6d0)"></div><div class="price">Prise : $ 11500</div><div class="desc">Lorem ipsum dolor sit</div><div class="info">Info ››</div></div>

<div class="abs bar" style="top:639px">UPCOMING AUCTIONS
  <div class="bar-arrows"><svg width="7" height="10"><path d="M5 1L2 5l3 4"/></svg><svg width="7" height="10"><path d="M2 1l3 4-3 4"/></svg></div>
</div>
<div class="abs card" style="left:80px;top:670px"><div class="thumb" role="img" aria-label="Suburban family house with driveway" style="background:linear-gradient(180deg,#3f7fc4,#d8d4c8 55%,#8a9a7a)"></div><div class="price">Prise : $ 15000</div><div class="desc">Lorem ipsum dolor sit</div><div class="info">Info ››</div></div>
<div class="abs card" style="left:201px;top:670px"><div class="thumb" role="img" aria-label="Brick townhouse with balconies" style="background:linear-gradient(180deg,#7aaede,#c7825a 55%,#6f8b55)"></div><div class="price">Prise : $ 14500</div><div class="desc">Lorem ipsum dolor sit</div><div class="info">Info ››</div></div>
<div class="abs card" style="left:322px;top:670px"><div class="thumb" role="img" aria-label="Row of beige homes under blue sky" style="background:linear-gradient(180deg,#5b95d2,#e4dcc4 55%,#8d9b78)"></div><div class="price">Prise : $ 14500</div><div class="desc">Lorem ipsum dolor sit</div><div class="info">Info ››</div></div>

<div class="abs testi-head">
  <svg width="24" height="20" viewBox="0 0 24 20"><rect x="1" y="3" width="17" height="15" rx="2" fill="none" stroke="#0b6b36" stroke-width="2"/><path d="M9 13l11-11 3 3-11 11-4 1z" fill="#333"/></svg>
  <h2>CLIENT TESTIMONIALS</h2>
</div>
<div class="abs testi-arrows"><svg width="8" height="12"><path d="M6 1L2 6l4 5" stroke="#999"/></svg><svg width="8" height="12"><path d="M2 1l4 5-4 5" stroke="#0b6b36"/></svg></div>
<div class="abs avatar" role="img" aria-label="Portrait of the client"></div>
<div class="abs testi-name">Mrs. Lena Marsh</div>
<div class="abs testi-role">Lorem Ipsum</div>
<p class="abs testi-quote"><span class="mark">❝</span>Utm tellus dolor, dapibus eget, elemen velmki cursus eleifelita arnean auctorbni wisi et urnam. Lorem ipsum dolor sit amet, conse ctetur adipiscing elit. Nulla in sollicitudin velit, bibendum velit.Cras vel facilisis ipsum, et venenatis risus.</p>

<aside>
  <div class="abs video-box">
    <div class="side-head">View Video
      <div class="bar-arrows" style="height:24px;right:6px"><svg width="7" height="10"><path d="M5 1L2 5l3 4"/></svg><svg width="7" height="10"><path d="M2 1l3 4-3 4"/></svg></div>
    </div>
    <div class="video-frame" role="img" aria-label="Video still of a model house on a laptop keyboard"><div class="play"><svg width="8" height="9"><path d="M0 0l8 4.5L0 9z" fill="#fff"/></svg></div></div>
    <div class="video-controls"><svg width="7" height="8"><path d="M0 0l7 4-7 4z" fill="#fff"/></svg><span>04:59</span><div class="track"></div><span>:0:35</span><svg width="9" height="8"><path d="M0 3h2l3-3v8L2 5H0z" fill="#fff"/></svg><svg width="9" height="9"><path d="M1 1l7 7M1 1h3M1 1v3M8 8H5M8 8V5" stroke="#fff" stroke-width="1.2"/></svg></div>
  </div>

  <div class="abs motd">
    <h3>Message of the Day</h3>
    <p>Lorem ipsum dolor sit amet ellit.Lorem ipsum dolor sit amet ellit.</p>
    <div class="abs motd-fold"></div>
    <svg width="6" height="9"><path d="M1 1l3.5 3.5L1 8"/></svg>
  </div>

  <div class="abs news">
    <div class="side-head">NEWS &amp; EVENTS<span class="view-all">View All</span></div>
    <div class="news-item sep" style="top:32px"><div class="date"><div class="day">01</div><div class="mon">MAY</div></div><div class="news-title">Lorem ipsum dolor</div><div class="news-text">Lorem ipsum dolor sit amet ellit Sit dolor</div><div class="news-more">Read More ››</div></div>
    <div class="news-item sep" style="top:81px"><div class="date"><div class="day">02</div><div class="mon">MAY</div></div><div class="news-title">Lorem ipsum dolor</div><div class="news-text">Lorem ipsum dolor sit amet ellit Sit dolor</div><div class="news-more">Read More ››</div></div>
    <div class="news-item sep" style="top:131px"><div class="date"><div class="day">03</div><div class="mon">MAY</div></div><div class="news-title">Lorem ipsum dolor</div><div class="news-text">Lorem ipsum dolor sit amet ellit Sit dolor</div><div class="news-more">Read More ››</div></div>
    <div class="news-item sep" style="top:180px"><div class="date"><div class="day">04</div><div class="mon">MAY</div></div><div class="news-title">Lorem ipsum dolor</div><div class="news-text">Lorem ipsum dolor sit amet ellit Sit dolor</div><div class="news-more">Read More ››</div></div>
    <div class="news-item" style="top:230px"><div class="date"><div class="day">05</div><div class="mon">MAY</div></div><div class="news-title">Lorem ipsum dolor</div><div class="news-text">Lorem ipsum dolor sit amet ellit Sit dolor</div><div class="news-more">Read More ››</div></div>
  </div>
</aside>

<footer>
  <div class="abs foot-band">
    <h4 style="left:81px">QUICK LINKS</h4>
    <h4 style="left:202px">OUR AFFILIATIONS</h4>
    <h4 style="left:340px">CONTACT DETAIL</h4>
    <h4 style="left:518px">NEWSLETTER</h4>
  </div>
  <div class="abs foot-dark"></div>
  <ul class="abs quick"><li>Home</li><li>All Auctions</li><li>Real Estate for Sale</li><li>Services</li><li>About Us</li><li>Contact Us</li></ul>
  <div class="abs aff"><span></span><span></span><span></span></div>
  <div class="abs fcontact">
    <div class="row" style="top:0;font-weight:700">BRANDT REAL ESTATE &amp; AUCTION</div>
    <div class="row" style="top:12px">5127 Old Harrow Lane, Alder Falls,</div>
    <div class="row" style="top:24px">NV 89410</div>
    <div class="row" style="top:46px"><svg width="8" height="8" viewBox="0 0 24 24"><path d="M6.6 10.8a15 15 0 0 0 6.6 6.6l2.2-2.2c.3-.3.7-.4 1-.2 1.1.4 2.3.6 3.6.6.6 0 1 .4 1 1V20c0 .6-.4 1-1 1A17 17 0 0 1 3 4c0-.6.4-1 1-1h3.5c.6 0 1 .4 1 1 0 1.3.2 2.5.6 3.6.1.3 0 .7-.2 1z"/></svg>270-555-3946</div>
    <div class="row" style="top:68px"><svg width="9" height="8" viewBox="0 0 9 8"><rect x="2" y="0" width="5" height="2"/><rect x="0" y="2.5" width="9" height="3.5" rx=".5"/><rect x="2" y="6" width="5" height="2"/></svg>270-555-3947</div>
    <div class="row" style="top:91px"><svg width="9" height="7" viewBox="0 0 9 7"><rect width="9" height="7" rx=".5"/><path d="M.5.5L4.5 4l4-3.5" stroke="#2b2b2b" fill="none"/></svg>info@brandtpropertybidhouse.example</div>
  </div>
  <div class="abs newsletter">Get Latest Updates By Entering<br>Your Email Address</div>
  <div class="field" style="top:1076px">Name</div>
  <div class="field" style="top:1100px">Email</div>
  <div class="abs submit">SUBMIT</div>
  <div class="abs foot-bottom"></div>
  <div class="abs copy">© 2015 BrandtRealEstate&amp;AuctionCo.All Rights Reserved. &nbsp;| &nbsp;Terms &amp; Conditions</div>
  <span class="abs social" style="left:563px"></span>
  <span class="abs social" style="left:586px"></span>
  <span class="abs social" style="left:609px"></span>
  <span class="abs social" style="left:632px"></span>
</footer>

</body>
</html>
```